BG & FTDL Tradeshow Backdrop Display

Backdrop Specs:
Size: 10ft wide x 10ft tall (Corvato Flat Display)
Shape: Flat back wall
Full-color dye-sublimation print

Goal:
Create a high-impact backdrop showcasing the partnership between Brightmoor Glow and Frost Top Deck Lamps. Design should attract attention from across the trade show floor, clearly explain what we offer, and reflect professionalism, holiday spirit, and partnership.

Content to Include:
Logos for two brands, placed prominently and equally and a picture of Milo Varga (owner of FrostTopDeckLamps "FTDL") and Derek Palm (owner of Brightmoor Glow "BG")

Headline (example):
“Nearly 50 Years of Combined Experience – Top-Tier Training & Industry-Leading Support”
or
“We Cover Everything: Training • Marketing • Products • Support”

Key Offerings (can be icons or short bullet list):
Rebate Programs
Hands-On Training
Sales & Marketing Support
Online Training Platform
Product Advancement Program
Operations & Team Management
Wholesale Pricing on Lighting & Décor

Imagery:
Training group photos, team member images, and festive lighting visuals.
Include FTDL elf mascot if it fits.
Milo (FTDL) is the photo of the man who has a beard.
Derek (BG) is the photo of the man who is in a tan jacket
I included 3 circular images of a Brightmoor Glow logo - this is our training logo. Please use only one that you feel will look the best on the design. We do not need all three.

Style & Colors:
Use each brand’s colors but make them blend harmoniously.
Festive holiday elements (twinkling lights, snowflakes, bokeh) as accents, not overpowering.
Professional yet approachable — balance fun (FTDL) with wholesale/training authority (Brightmoor Glow, BGA).
Brightmoor Glow branding colors: #0072bb (primary), #f59426 (secondary)
FrostTopDeckLamps branding colors: #e82520 (primary), #1f6c39 (secondary)
Looking for a modern design.

Design Notes:
Keep text readable from 10–15 feet away.
Place key content at/above eye level for visibility.
Leave lower portion cleaner for booth furniture in front.
Background can subtly fade to highlight text and logos.

References Provided:
Partnership flyer (text, logos, photo ideas, color inspiration)
VEX Banners example (format and proportions)

Target Market(s)

Entrepreneurs

Industry/Entity Type

Wholesale & Distribution

Colors
0054AA
0677BA
7BADD7
CADEEF
E8F1F8
00AB8E
00BBA5
67D7C9
C6EFE9
E9F9F6
FFC000
F8CF3A
FAE287
FDF2CF
FEFAEE
EB3D1F
EC4F4E
F09395
F8D3D4
FCEDEE

Requirements
Must have
• A modern feel with Christmas vibes entangling the two brands.
Nice to have
• Fun Christmas decor like snowflakes, snow, or other common Christmas theme decor - maybe Santa with a sleigh?
Should not have
• Nothing exact

```html
<!DOCTYPE html>
<html lang="en">
<head>
<meta charset="utf-8">
<title>BG &amp; FTDL Tradeshow Backdrop</title>
<link rel="stylesheet" href="https://fonts.googleapis.com/css2?family=Stardos+Stencil:wght@700&family=Arimo:wght@400;700&display=swap">
<style>
  :root {
    --stage: #eeeeee;
    --paper: #f7f5f0;
    --festive-red: #e82520;
    --festive-green: #1f6c39;
    --brand-blue: #0a6fb8;
    --brand-orange: #f59426;
    --white: #ffffff;
    --ink-soft: #5b5b5b;
  }
  * { box-sizing: border-box; margin: 0; padding: 0; }
  html, body { width: 1200px; height: 960px; overflow: hidden; }
  body {
    background: var(--stage);
    font-family: "Arimo", Arial, sans-serif;
    position: relative;
  }
  .backdrop {
    position: absolute;
    left: 100px; top: 40px;
    width: 1000px; height: 880px;
    border-radius: 18px;
    overflow: hidden;
    background: var(--paper);
    box-shadow: 0 6px 24px rgba(0,0,0,.15);
  }
  .backdrop__bokeh {
    position: absolute; inset: 0 0 400px 0;
    background:
      radial-gradient(circle at 8% 6%, rgba(255,230,160,.8) 0 22px, transparent 40px),
      radial-gradient(circle at 30% 3%, rgba(255,230,160,.7) 0 18px, transparent 36px),
      radial-gradient(circle at 55% 6%, rgba(255,230,160,.7) 0 18px, transparent 36px),
      radial-gradient(circle at 78% 2%, rgba(255,230,160,.6) 0 16px, transparent 32px),
      linear-gradient(180deg, #f3efe6 0%, #faf9f6 60%, #f1ede4 100%);
  }
  .headline {
    position: absolute; left: 70px; top: 70px;
    font-family: "Stardos Stencil", "Georgia", serif;
    font-weight: 700;
    color: var(--festive-red);
    font-size: 56px;
    line-height: 1.05;
    letter-spacing: 1px;
  }
  .headline__row { display: flex; align-items: center; gap: 10px; }
  .headline__badge {
    display: inline-flex; align-items: center; justify-content: center;
    width: 130px; height: 74px;
    border-radius: 50%;
    background: var(--festive-green);
    color: var(--white);
    font-size: 58px;
  }
  .brands {
    position: absolute; right: 40px; top: 48px;
    display: flex; gap: 26px; align-items: center;
  }
  .brands__name {
    font-family: "Arimo", Arial, sans-serif;
    font-weight: 700;
    font-size: 19px;
    display: flex; align-items: center; gap: 8px;
  }
  .brands__name--ftdl { color: var(--festive-green); }
  .brands__name--bg { color: var(--brand-blue); }
  .brands__mark { width: 14px; height: 14px; border-radius: 50%; background: currentColor; }
  .visual {
    position: absolute;
  }
  .visual--decor {
    left: 0; top: 250px; width: 380px; height: 230px;
    background: radial-gradient(circle at 40% 60%, #c99a4a 0 40px, transparent 90px),
                linear-gradient(135deg, #3f6b2f 0%, #7a8f3c 55%, rgba(247,245,240,0) 100%);
    opacity: .85;
  }
  .visual--derek {
    left: 440px; top: 130px; width: 260px; height: 350px;
    background: linear-gradient(180deg, #e3c9a6 0%, #bfa070 45%, #5a7db0 100%);
    border-radius: 120px 120px 0 0;
  }
  .visual--milo {
    left: 700px; top: 120px; width: 260px; height: 360px;
    background: linear-gradient(180deg, #b38866 0%, #d9c2aa 40%, #f2f2f2 100%);
    border-radius: 120px 120px 0 0;
  }
  .band {
    position: absolute; left: 0; right: 0; top: 480px; bottom: 0;
    background: var(--brand-blue);
    border-top: 6px solid var(--brand-orange);
    color: var(--white);
  }
  .coverage {
    position: absolute; left: 90px; top: 40px;
    display: flex; gap: 34px; align-items: flex-start;
  }
  .coverage__lead { font-size: 28px; font-weight: 700; margin-top: 8px; }
  .coverage__list {
    color: var(--brand-orange);
    font-size: 27px; font-weight: 700;
  }
  .coverage__icons { display: flex; gap: 58px; margin-top: 12px; margin-left: 30px; }
  .coverage__icons svg { width: 44px; height: 40px; stroke: var(--white); fill: none; stroke-width: 2.2; stroke-linecap: round; stroke-linejoin: round; }
  .offerings { position: absolute; left: 90px; top: 150px; right: 60px; }
  .offerings__title { color: var(--brand-orange); font-size: 32px; font-weight: 700; margin-bottom: 16px; }
  .offerings__cols { display: flex; gap: 60px; }
  .offerings__list { list-style: none; font-size: 23px; line-height: 1.45; }
  .offerings__list li::before { content: "•"; margin-right: 10px; }
  .offerings__list--right { margin-top: -48px; }
</style>
</head>
<body>
  <main class="backdrop">
    <div class="backdrop__bokeh" role="img" aria-label="Soft background of warm holiday string-light bokeh"></div>

    <h1 class="headline">
      <span class="headline__row">NEARLY <span class="headline__badge">50</span> YEARS</span>
      <span class="headline__row">OF COMBINED</span>
      <span class="headline__row">EXPERIENCE</span>
    </h1>

    <div class="brands">
      <span class="brands__name brands__name--ftdl"><span class="brands__mark"></span>Frost Top Deck Lamps</span>
      <span class="brands__name brands__name--bg">Brightmoor Glow</span>
    </div>

    <div class="visual visual--decor" role="img" aria-label="Festive pine branches with gold Christmas ornaments"></div>
    <div class="visual visual--derek" role="img" aria-label="Photo of Derek Palm in a tan jacket"></div>
    <div class="visual visual--milo" role="img" aria-label="Photo of Milo Varga, bearded, arms crossed"></div>

    <section class="band">
      <div class="coverage">
        <p class="coverage__lead">We Cover Everything:</p>
        <div>
          <p class="coverage__list">Training • Marketing • Products • Support</p>
          <div class="coverage__icons">
            <svg viewBox="0 0 44 40" aria-hidden="true"><circle cx="22" cy="10" r="5"/><circle cx="9" cy="16" r="4"/><circle cx="35" cy="16" r="4"/><path d="M12 34c0-8 20-8 20 0M2 32c0-6 12-7 12-3M42 32c0-6-12-7-12-3"/></svg>
            <svg viewBox="0 0 44 40" aria-hidden="true"><path d="M6 16h8l18-9v26l-18-9H6z"/><path d="M12 24l3 10h5l-2-10"/><path d="M37 14l4-3M38 20h5M37 26l4 3"/></svg>
            <svg viewBox="0 0 44 40" aria-hidden="true"><path d="M6 12l16-8 16 8v18l-16 8-16-8z"/><path d="M6 12l16 8 16-8M22 20v18"/></svg>
            <svg viewBox="0 0 44 40" aria-hidden="true"><path d="M4 18l8-8 8 4 6-4 14 10-12 12-8-6-4 2-12-10z"/><path d="M20 14l-6 6 4 3 6-5"/></svg>
          </div>
        </div>
      </div>

      <div class="offerings">
        <h2 class="offerings__title">Key Offerings</h2>
        <div class="offerings__cols">
          <ul class="offerings__list">
            <li>Rebate Programs</li>
            <li>Sales &amp; Marketing Support</li>
            <li>Product Advancement Program</li>
            <li>Wholesale Pricing on Lighting</li>
          </ul>
          <ul class="offerings__list offerings__list--right">
            <li>Hands-On Training</li>
            <li>Online Training Platform</li>
            <li>Operations &amp; Team Management</li>
            <li>&amp; Décor</li>
          </ul>
        </div>
      </div>
    </section>
  </main>
</body>
</html>
```